Town's Facebook Cover Photo / Banner

We are launching a new town Facebook Page. The name of the page is:
The Fernwicker , its is intended to be the digiatal "town square" for the residence of Fernwick, a very quaint suburan town in NJ.

Would like the words "Town Squre" to be prominent displayed on the Cover photo

Also need to include our Slogan: "Your Community, Your Future, Your Fernwick!"

Target Market(s)

The local Towns People of Fernwick Only

Number of Pages Required

1 page

Requirements
Must have
• The Fernwicker Prominently Displayed

```html
<!DOCTYPE html>
<html lang="en">
<head>
<meta charset="UTF-8">
<title>The Fernwicker – Town Square Cover</title>
<link href="https://fonts.googleapis.com/css2?family=Inter:wght@700;800&family=Great+Vibes&display=swap" rel="stylesheet">
<style>
  :root {
    --bg: #d3dde3;
    --sky: #3f78b8;
    --sky-light: #9cc0e0;
    --foliage: #3c4a22;
    --foliage-dark: #252d15;
    --rock: #9a6a44;
    --circle: rgba(22, 58, 22, 0.88);
    --text: #ffffff;
    --script: #e6ecd8;
    --seal-bg: #f4f4f2;
    --seal-ink: #2a2a2a;
  }
  * { margin: 0; padding: 0; box-sizing: border-box; }
  html, body { width: 1200px; height: 900px; overflow: hidden; background: var(--bg); }
  .canvas { position: relative; width: 1200px; height: 900px; }
  .cover {
    position: absolute; left: 50px; top: 230px; width: 1100px; height: 400px;
    overflow: hidden;
  }
  .cover-photo {
    position: absolute; inset: 0;
    background:
      linear-gradient(90deg, rgba(37,45,21,0) 0%, rgba(37,45,21,0) 62%, rgba(154,106,68,0.95) 75%, rgba(120,80,50,1) 100%),
      linear-gradient(180deg, var(--sky) 0%, var(--sky-light) 22%, var(--foliage) 40%, var(--foliage-dark) 78%, #6b5a3a 100%);
  }
  .title-circle {
    position: absolute; left: 285px; top: -3px; width: 530px; height: 530px;
    border-radius: 50%; background: var(--circle);
  }
  .title {
    position: absolute; left: 0; right: 0; top: 78px; text-align: center;
    color: var(--text); font-family: 'Inter', sans-serif;
  }
  .title-name { font-size: 58px; font-weight: 800; line-height: 1; letter-spacing: -0.5px; }
  .title-script {
    display: block; font-family: 'Great Vibes', cursive; font-weight: 400;
    font-size: 52px; color: var(--script); line-height: 0.9; margin-top: -4px;
  }
  .title-main { font-size: 62px; font-weight: 800; line-height: 1; margin-top: 12px; letter-spacing: -0.5px; }
  .slogan { font-size: 21px; font-weight: 700; margin-top: 24px; }
  .seal {
    position: absolute; left: 206px; top: 536px; width: 188px; height: 188px;
    border-radius: 50%; background: var(--seal-bg);
    border: 5px solid var(--seal-ink);
    display: flex; align-items: center; justify-content: center; text-align: center;
    font-family: 'Inter', sans-serif; font-weight: 700; font-size: 18px; color: var(--seal-ink);
    line-height: 1.2; padding: 20px;
  }
</style>
</head>
<body>
  <div class="canvas">
    <section class="cover">
      <div class="cover-photo" role="img" aria-label="Photo of a town corner with trees, a house, an American flag on a pole and a large boulder under a blue sky"></div>
      <div class="title-circle"></div>
      <div class="title">
        <div class="title-name">The Fernwicker</div>
        <span class="title-script">Town Page</span>
        <div class="title-main">Town Square</div>
        <div class="slogan">Your Community, Your Future, Your Fernwick!</div>
      </div>
    </section>
    <div class="seal">Borough of Fernwick</div>
  </div>
</body>
</html>
```